Kestrel Arc Services business card Design

I need a business card that will wow clients at first sight.

Kestrel Arc Services connects people with HOME & LIFESTYLE SERVICES, and the client pays the value that was created by our service, using. 'Settle On The Sum That Feels Fair".
Please look us up at www.kestrelarcservices.example to see our mission and services.

The new website is being launched in 8 weeks.

I need a business card to campaign LANDSCAPING however please design it to be easily modified to CLEANING SERVICE, PLUMBING Etc Etc.

Until our SEO campaign begins working I need business cards to leave with prospective clients for each individual service as appropriate.

Dorian Maltby
Creative Director
www.kestrelarcservices.example
1-888-517-4KAS
email: info@kestrelarcservices.example

Target Market(s)

Residential and commercial clients

Industry/Entity Type

Business

Contact Information for Business Card

2 sided

Font styles to use
Sans Serif

Requirements
Must have
• Im prefering a black card so far
• Logo
• "Settle On The Sum That Feels Fair" seal
• Complete Landscaping & Construction
• Tarnwell Services
• Contact details
• facebook kestrelarc services
• twitter @kestrelarc services
• Adaptable card easily to different services we offer at Kestrel Arc Services as per www.kestrelarcservices.example
Should not have
• Too much imagery

```html
<!DOCTYPE html>
<html lang="en">
<head>
<meta charset="utf-8">
<title>Kestrel Arc Services – Business Card</title>
<link rel="stylesheet" href="https://fonts.googleapis.com/css2?family=Montserrat:wght@400;700&family=Lato:wght@400;700&display=swap">
<style>
  :root {
    --page-bg: #e9e7e3;
    --card-dark: #1c1d1f;
    --card-dark-2: #2a2b2e;
    --green: #1fae4a;
    --teal: #17c2b2;
    --sky: #3cc3ec;
    --violet: #8a7fd9;
    --white: #ffffff;
    --muted: #c9ccd1;
    --accent-green: #7bd34a;
    --dot: #3f7fd4;
  }
  * { margin: 0; padding: 0; box-sizing: border-box; }
  html, body { width: 1200px; height: 913px; overflow: hidden; }
  body {
    background: var(--page-bg);
    font-family: "Lato", sans-serif;
    display: flex;
    flex-direction: column;
    align-items: center;
    justify-content: center;
    gap: 56px;
  }
  .card {
    position: relative;
    width: 630px;
    height: 360px;
    border-radius: 4px;
    overflow: hidden;
    box-shadow: 0 10px 28px rgba(0,0,0,0.22);
  }
  .card svg.card-art { position: absolute; inset: 0; width: 100%; height: 100%; }

  .brand {
    position: absolute;
    display: flex;
    align-items: center;
    gap: 10px;
  }
  .brand-mark {
    width: 22px; height: 22px; border-radius: 50%;
    background: var(--dot);
    flex: none;
  }
  .brand-name {
    font-family: "Montserrat", sans-serif;
    font-weight: 400;
    color: var(--white);
    font-size: 24px;
    white-space: nowrap;
  }

  /* front */
  .card-front .brand { left: 158px; top: 166px; }

  /* back */
  .card-back { background: linear-gradient(160deg, var(--card-dark-2), var(--card-dark) 60%); }
  .card-back .brand { left: 32px; top: 48px; }
  .card-back .brand-name { font-size: 21px; }
  .services {
    position: absolute; left: 32px; top: 104px;
    color: var(--white);
    font-family: "Montserrat", sans-serif;
    font-size: 12px;
    line-height: 1.6;
    text-transform: uppercase;
  }
  .services .service-main { color: var(--accent-green); font-weight: 700; }
  .seal {
    position: absolute; left: 32px; top: 178px;
    display: flex; align-items: center; gap: 10px;
    color: var(--white);
    font-size: 12px;
    font-style: normal;
    max-width: 310px;
  }
  .seal-badge {
    width: 44px; height: 44px; border-radius: 50%;
    border: 3px solid var(--accent-green);
    flex: none;
  }
  .divider {
    position: absolute; left: 360px; top: 30px;
    width: 1px; height: 205px; background: var(--muted);
  }
  .contact { position: absolute; left: 378px; top: 34px; color: var(--white); }
  .person-name {
    font-family: "Montserrat", sans-serif;
    font-size: 22px;
    text-transform: uppercase;
    line-height: 1;
    white-space: nowrap;
  }
  .person-name .first { font-weight: 700; }
  .person-name .last { font-weight: 400; }
  .person-role {
    font-family: "Montserrat", sans-serif;
    color: var(--accent-green);
    font-size: 11px;
    text-transform: uppercase;
    margin-top: 5px;
  }
  .contact-list { list-style: none; margin-top: 16px; font-size: 11.5px; }
  .contact-list li { display: flex; align-items: center; gap: 9px; margin-bottom: 9px; white-space: nowrap; }
  .contact-list svg { width: 13px; height: 13px; flex: none; }
  .social-label { color: var(--accent-green); min-width: 52px; }
  .band {
    position: absolute; left: 0; right: 0; bottom: 0; height: 96px;
    background: linear-gradient(90deg, var(--green), var(--teal) 45%, var(--sky) 78%, var(--violet));
    clip-path: polygon(0 22%, 100% 0, 100% 100%, 0 100%);
  }
</style>
</head>
<body>

  <section class="card card-front" aria-label="Card front">
    <svg class="card-art" viewBox="0 0 630 360" preserveAspectRatio="none" aria-hidden="true">
      <defs>
        <linearGradient id="front-grad" x1="0" y1="1" x2="1" y2="0">
          <stop offset="0" stop-color="#1fae4a"/>
          <stop offset="0.45" stop-color="#17c2b2"/>
          <stop offset="0.75" stop-color="#3cc3ec"/>
          <stop offset="1" stop-color="#8a7fd9"/>
        </linearGradient>
      </defs>
      <rect width="630" height="360" fill="url(#front-grad)"/>
      <polygon class="ribbon-tail" points="20,250 560,120 600,150 70,290" fill="rgba(24,30,32,0.82)"/>
      <polygon class="ribbon-panel" points="120,80 490,40 520,270 150,320" fill="rgba(28,32,34,0.88)"/>
    </svg>
    <div class="brand">
      <span class="brand-mark"></span>
      <span class="brand-name">Kestrel Arc Services Inc.</span>
    </div>
  </section>

  <section class="card card-back" aria-label="Card back">
    <div class="brand">
      <span class="brand-mark"></span>
      <span class="brand-name">Kestrel Arc Services Inc.</span>
    </div>
    <div class="services">
      <p class="service-main">Complete Landscaping &amp; Construction</p>
      <p class="service-sub">Tarnwell Services</p>
    </div>
    <div class="seal">
      <span class="seal-badge" aria-hidden="true"></span>
      <span class="seal-text">"Settle On The Sum That Feels Fair"</span>
    </div>
    <div class="divider"></div>
    <div class="contact">
      <p class="person-name"><span class="first">Dorian</span> <span class="last">Maltby</span></p>
      <p class="person-role">Creative Director</p>
      <ul class="contact-list">
        <li>
          <svg viewBox="0 0 16 16" aria-hidden="true"><path fill="#fff" d="M2 5c0-2 3-3 6-3s6 1 6 3v1h-3V5H5v1H2z M4 7h8l2 6H2z"/></svg>
          1-888-517-4KAS
        </li>
        <li>
          <svg viewBox="0 0 16 16" aria-hidden="true"><rect x="1" y="3" width="14" height="10" fill="#fff"/><path d="M1 3l7 6 7-6" stroke="#1c1d1f" stroke-width="1.4" fill="none"/></svg>
          info@kestrelarcservices.example
        </li>
        <li>
          <svg viewBox="0 0 16 16" aria-hidden="true"><g fill="none" stroke="#fff" stroke-width="1.3"><circle cx="8" cy="8" r="6.5"/><ellipse cx="8" cy="8" rx="3" ry="6.5"/><path d="M1.5 8h13M2.5 5h11M2.5 11h11"/></g></svg>
          www.kestrelarcservices.example
        </li>
        <li><span class="social-label">facebook</span> kestrelarc services</li>
        <li><span class="social-label">twitter</span> @kestrelarc services</li>
      </ul>
    </div>
    <div class="band"></div>
  </section>

</body>
</html>
```